Website Design for Business Law Firm

We have a logo and now we would like a web site design for our new website. Our small firm provides creative and aggressive transactional (not litigation) legal services to advise healthcare, technology, internet-based and traditional companies and investors in such companies on healthcare, technology, financing, mergers/acquisitions, real estate and other transactions, legal compliance and general corporate and business matters.

We would like to see a website design that is professional and appropriate for executives, professionals, investors and government regulators to visit, that conveys professionalism and competence while being a little edgy and modern - no typical legal motifs such as gavels, books, or scales of justice. We advise businesses and investors and guide them through complicated issues quickly, capably and differently from other law firms. We are part of the business team and get things done.

The logo is attached, and we like gray as a color to complement it. The intention of the logo is to convey that in a storm or challenging time, people come to this firm, and people come to this firm when they need the power and disruption to change things or shake them up.

I have also enclosed a picture of our business card for consideration.

On the other hand, you can check out the current simple site at www.venhollow.example to see we have used a space motif in the past to evoke that we help create stars (the nebula featured there). This is not a necessary part of the new website and it may look better without it.

We appreciate your creativity and look forward to designs.

Industry/Entity Type

Business

Requirements
Must have
• We anticipate the following pages, and you may submit different ideas for the different pages:
• 1. Landing page
• 2. Services pages - healthcare, IT/Technology, general counsel services, financings, mergers/acquisitions, mediation/arbitration, procurement and productization
• 3. About Us including contact information
• Our name and contact information:
• Quellane Law Firm, P.C.
• 8716 SW 19th Ave.
• Portland, OR 97213
• phone: 971.555.0143
• fax: 971.555.0187
Nice to have
• Please consider designs that enhance the impressions we are looking for
Should not have
• Please no gavels, scales of justice, law books, or similar traditional legal imagery.

```html
<!DOCTYPE html>
<html lang="en">
<head>
<meta charset="utf-8">
<title>Quellane Law Firm, P.C.</title>
<link rel="stylesheet" href="https://fonts.googleapis.com/css2?family=Questrial&family=Open+Sans:ital,wght@0,400;0,600;1,700&display=swap">
<style>
:root{
  --page:#2a2a2a;
  --band:#353535;
  --teal:#527276;
  --teal-dark:#46656a;
  --ink-dark:#1e2729;
  --white:#ffffff;
  --text:#3a3a3a;
  --light:#e6e6e6;
  --muted:#9a9a9a;
  --dash:#5a5a5a;
}
*{margin:0;padding:0;box-sizing:border-box}
html,body{width:990px;height:1200px;overflow:hidden;background:var(--page)}
body{position:relative;font-family:"Open Sans",sans-serif;color:var(--light)}
.abs{position:absolute}
.display{font-family:"Questrial",sans-serif}

/* header */
.brand{left:179px;top:36px;width:170px;height:42px;display:flex;align-items:center;gap:8px;font-family:"Questrial",sans-serif;font-size:26px;letter-spacing:5px;color:var(--light)}
.brand-square{width:12px;height:12px;background:var(--teal)}
.top-phone{left:672px;top:22px;display:flex;align-items:center;gap:8px;font-family:"Questrial",sans-serif;font-size:18px;color:var(--white)}
.icon-dot{width:20px;height:20px;border-radius:50%;background:var(--teal);display:flex;align-items:center;justify-content:center}
.main-nav{left:380px;top:57px;display:flex;align-items:center;font-family:"Questrial",sans-serif;font-size:11px;color:var(--white)}
.main-nav a{color:inherit;text-decoration:none;padding:0 12px;height:24px;line-height:24px;display:flex;align-items:center;gap:6px}
.main-nav a.active{background:var(--teal)}

/* hero */
.hero{left:114px;top:102px;width:762px;height:344px;background:radial-gradient(ellipse at 35% 50%,#4a4a4a 0%,#3a3a3a 55%,#2e2e2e 100%);overflow:hidden}
.hero-photo{position:absolute;left:398px;top:0;width:364px;height:344px;background:linear-gradient(180deg,#4b4a48 0%,#2d2c2c 55%,#1e1e1f 100%)}
.hero-title{left:178px;top:184px;font-size:21px;line-height:26px;letter-spacing:.5px;color:var(--white)}
.hero-list{top:246px;list-style:none;font-size:12px;line-height:19px;color:var(--white)}
.hero-list li{display:flex;align-items:center;gap:6px}
.cta{left:178px;top:320px;width:328px;height:38px;background:var(--teal);color:var(--white);font-family:"Questrial",sans-serif;font-size:22px;letter-spacing:1.5px;display:flex;align-items:center;justify-content:center;box-shadow:0 2px 3px rgba(0,0,0,.4)}
.hero-more{left:430px;top:367px;font-size:10.5px;letter-spacing:1px;color:var(--white)}

/* welcome band */
.welcome{left:114px;top:446px;width:762px;height:294px;background:var(--white)}
.welcome-title{left:178px;top:480px;font-size:26px;color:var(--text)}
.welcome-rule{left:178px;top:514px;width:264px;height:1px;background:#9a9a9a}
.welcome-text{left:178px;top:520px;width:264px;font-size:10.4px;line-height:14.8px;color:var(--text)}
.small-btn{left:367px;top:665px;width:76px;height:15px;background:var(--teal);color:var(--white);font-size:8.5px;letter-spacing:.8px;display:flex;align-items:center;justify-content:center}

.contact-box{left:469px;top:482px;width:341px;height:200px;background:var(--teal)}
.contact-head{left:529px;top:505px;font-size:12px;line-height:13px;color:var(--white)}
.field{background:var(--white);border:1px solid #c9d3d4;font-size:8.5px;color:#8a8a8a;padding:4px 6px}
.submit{left:487px;top:630px;width:142px;height:30px;background:var(--ink-dark);color:var(--white);font-family:"Questrial",sans-serif;font-size:21px;letter-spacing:1px;display:flex;align-items:center;justify-content:center}

/* news & practices */
.news-tab{left:178px;top:777px;width:124px;height:21px;background:var(--white);color:#222;font-size:11.5px;letter-spacing:-.3px;padding-left:12px;line-height:21px;clip-path:polygon(0 0,100% 0,96% 50%,100% 100%,0 100%)}
.news-item{left:177px;width:260px;font-size:10.8px;line-height:12px;color:var(--white)}
.news-date{font-style:italic;font-weight:700;letter-spacing:.5px;margin-bottom:1px}
.news-body{padding-left:2px}
.section-title{left:469px;top:781px;font-size:12.5px;letter-spacing:.3px;color:var(--white)}
.arrow{top:779px;width:19px;height:19px;border-radius:50%;display:flex;align-items:center;justify-content:center}
.practices-text{left:470px;top:813px;width:340px;font-size:10.2px;line-height:12.5px;color:var(--white)}
.practice{top:849px;width:101px}
.practice-img{width:101px;height:97px}
.practice-label{text-align:center;font-size:11.5px;margin-top:4px;color:var(--white)}

/* footer */
.dash{left:114px;width:762px;height:0;border-top:1px dashed var(--dash)}
.foot-nav{left:180px;top:1001px;display:flex;gap:13px;font-size:9px;color:var(--white)}
.foot-phone{left:656px;top:999px;display:flex;align-items:center;gap:6px;font-family:"Questrial",sans-serif;font-size:15px;color:var(--white)}
.social{width:9px;height:9px;border-radius:50%;background:var(--teal)}
.foot-list{top:1041px;list-style:none;font-size:8.6px;line-height:12.3px;color:var(--muted)}
.foot-list li{padding-left:5px;position:relative}
.foot-list li::before{content:"›";position:absolute;left:0}
.foot-brand{left:662px;top:1046px;width:148px;height:34px;display:flex;align-items:center;justify-content:center;gap:7px;font-family:"Questrial",sans-serif;font-size:19px;letter-spacing:5px;color:var(--light);background:#333}
.copyright{left:664px;top:1084px;font-size:8.6px;color:var(--white)}
</style>
</head>
<body>

<header>
  <div class="abs brand"><span class="brand-square"></span>QUELLANE</div>
  <div class="abs top-phone">
    <span class="icon-dot"><svg width="11" height="10" viewBox="0 0 11 10"><rect x="3" y="0" width="5" height="3" fill="#fff"/><rect x="0" y="3" width="11" height="4" rx="1" fill="#fff"/><rect x="3" y="6" width="5" height="4" fill="#fff" stroke="#527276" stroke-width=".8"/></svg></span>
    971.555.0187
  </div>
  <nav class="abs main-nav">
    <a href="#"><svg width="11" height="10" viewBox="0 0 11 10"><path d="M5.5 0 11 5H9.5v5h-3V7h-2v3h-3V5H0z" fill="#fff"/></svg>OUR PRECTICES</a>
    <a href="#" class="active">PROFESSIONALS</a>
    <a href="#">CAREERS</a>
    <a href="#">ABOUT US</a>
    <a href="#">CONTACT</a>
  </nav>
</header>

<section class="abs hero">
  <div class="hero-photo" role="img" aria-label="Photo of two smiling business professionals in dark suits with arms crossed"></div>
</section>
<h1 class="abs display hero-title" style="font-weight:400">PRAGMATIC, CREATIVE SERVICES<br>FOR INNOVATIVE BUSINESSES</h1>
<ul class="abs hero-list" style="left:178px">
  <li><svg width="9" height="9" viewBox="0 0 10 10"><circle cx="5" cy="5" r="4.2" fill="none" stroke="#fff" stroke-width="1.2"/><path d="M3 5.2 4.5 6.6 7 3.8" fill="none" stroke="#fff" stroke-width="1.2"/></svg>Strategic Alliances</li>
  <li><svg width="9" height="9" viewBox="0 0 10 10"><circle cx="5" cy="5" r="4.2" fill="none" stroke="#fff" stroke-width="1.2"/><path d="M3 5.2 4.5 6.6 7 3.8" fill="none" stroke="#fff" stroke-width="1.2"/></svg>Business Relationships</li>
  <li><svg width="9" height="9" viewBox="0 0 10 10"><circle cx="5" cy="5" r="4.2" fill="none" stroke="#fff" stroke-width="1.2"/><path d="M3 5.2 4.5 6.6 7 3.8" fill="none" stroke="#fff" stroke-width="1.2"/></svg>Outsourcing</li>
</ul>
<ul class="abs hero-list" style="left:328px">
  <li><svg width="9" height="9" viewBox="0 0 10 10"><circle cx="5" cy="5" r="4.2" fill="none" stroke="#fff" stroke-width="1.2"/><path d="M3 5.2 4.5 6.6 7 3.8" fill="none" stroke="#fff" stroke-width="1.2"/></svg>Procurements - Buying or Selling</li>
  <li><svg width="9" height="9" viewBox="0 0 10 10"><circle cx="5" cy="5" r="4.2" fill="none" stroke="#fff" stroke-width="1.2"/><path d="M3 5.2 4.5 6.6 7 3.8" fill="none" stroke="#fff" stroke-width="1.2"/></svg>Licensing and Technology Exploitation</li>
  <li><svg width="9" height="9" viewBox="0 0 10 10"><circle cx="5" cy="5" r="4.2" fill="none" stroke="#fff" stroke-width="1.2"/><path d="M3 5.2 4.5 6.6 7 3.8" fill="none" stroke="#fff" stroke-width="1.2"/></svg>Venture Formation and Startup</li>
</ul>
<div class="abs cta">-&nbsp; CALL TO ACTION &nbsp;-</div>
<div class="abs hero-more">Learn More &gt;&gt;</div>

<section class="abs welcome"></section>
<h2 class="abs display welcome-title" style="font-weight:400">Welcome to Quellane</h2>
<div class="abs welcome-rule"></div>
<p class="abs welcome-text">Lorem ipsum dolor sit amet, consectetur adipiscing elit. In fermentum dolor non augue pretium egestas. Donec sem eros, tincidunt at congue ut, posuere sit amet est. Vivamus scelerisque viverra odio sit amet laoreet. Ut nec neque non justo rutrum tempor lobortis eu ante.&nbsp; dolor Aliquam sagittis, nibh quis commodo auctor, risus nibh mauris laoreet lectus, id facilisis libero odio nec enim. Sed id ligula adipiscing purus lacinia aliquet. Sed eu est non nisl vehicula bibendum congue sit amet enim.</p>
<div class="abs small-btn">Learn More</div>

<div class="abs contact-box"></div>
<svg class="abs" style="left:488px;top:506px" width="32" height="24" viewBox="0 0 32 24"><rect x="1" y="1" width="30" height="22" fill="none" stroke="#fff" stroke-width="1.5"/><path d="M1 1 16 13 31 1M1 23 12 10M31 23 20 10" fill="none" stroke="#fff" stroke-width="1.5"/></svg>
<div class="abs display contact-head">FASTER GET IN TOUCH HERE!<br>WITH QUELLANE</div>
<div class="abs field" style="left:488px;top:546px;width:152px;height:20px">Name</div>
<div class="abs field" style="left:488px;top:571px;width:152px;height:20px">Email</div>
<div class="abs field" style="left:488px;top:597px;width:152px;height:20px">Phone</div>
<div class="abs field" style="left:644px;top:546px;width:145px;height:70px">Comments</div>
<div class="abs submit">SUBMIT</div>

<div class="abs news-tab">LATEST NEWS</div>
<article class="abs news-item" style="top:811px"><div class="news-date">05 DEC, 2013</div><div class="news-body">Lorem ipsum dolor sit amet, consectetur adipiscing elit. In fermentum congue .. Read More</div></article>
<article class="abs news-item" style="top:857px"><div class="news-date">05 DEC, 2013</div><div class="news-body">Lorem ipsum dolor sit amet, consectetur adipiscing elit. In fermentum congue .. Read More</div></article>
<article class="abs news-item" style="top:905px"><div class="news-date">05 DEC, 2013</div><div class="news-body">Lorem ipsum dolor sit amet, consectetur adipiscing elit. In fermentum congue .. Read More</div></article>

<div class="abs display section-title">OUR PRACTICES AREAS</div>
<div class="abs arrow" style="left:767px;background:var(--teal)"><svg width="8" height="8" viewBox="0 0 8 8"><path d="M5.5 1 2.5 4 5.5 7" fill="none" stroke="#fff" stroke-width="1.6"/></svg></div>
<div class="abs arrow" style="left:791px;background:#111;border:1px solid #555"><svg width="8" height="8" viewBox="0 0 8 8"><path d="M2.5 1 5.5 4 2.5 7" fill="none" stroke="#fff" stroke-width="1.6"/></svg></div>
<p class="abs practices-text">Lorem ipsum dolor sit amet, consectetur adipiscing elit. In fermen dolor tum dolor non augue pretium egestas consectetur</p>
<div class="abs practice" style="left:470px"><div class="practice-img" role="img" aria-label="Photo of a healthcare worker assisting a patient with exercise weights" style="background:linear-gradient(135deg,#e9e4e6,#c9a0b4 60%,#b04a8a)"></div><div class="practice-label">HealthCare</div></div>
<div class="abs practice" style="left:589px"><div class="practice-img" role="img" aria-label="Photo of business people talking in a bright office lobby" style="background:linear-gradient(180deg,#dfe8ee,#aebfcb 60%,#4a5058)"></div><div class="practice-label">Businesses</div></div>
<div class="abs practice" style="left:708px"><div class="practice-img" role="img" aria-label="Photo of a hand touching a digital interface screen" style="background:linear-gradient(135deg,#d9dee2,#a9b4bc 60%,#7d8a94)"></div><div class="practice-label">Technology</div></div>

<footer>
  <div class="abs dash" style="top:994px"></div>
  <nav class="abs foot-nav"><span>Our Prectices</span><span>Professionals</span><span>Careers</span><span>About us</span><span>Contact</span></nav>
  <div class="abs foot-phone">
    <svg width="12" height="11" viewBox="0 0 11 10"><rect x="3" y="0" width="5" height="3" fill="#fff"/><rect x="0" y="3" width="11" height="4" rx="1" fill="#fff"/><rect x="3" y="6" width="5" height="4" fill="#fff" stroke="#2a2a2a" stroke-width=".8"/></svg>
    971.555.0187 <span class="social"></span><span class="social"></span>
  </div>
  <div class="abs dash" style="top:1023px"></div>
  <ul class="abs foot-list" style="left:179px"><li>Strategic Alliances</li><li>Business Relationships</li><li>Outsourcing</li><li>Procurements -<br>Buying or Selling</li></ul>
  <ul class="abs foot-list" style="left:301px"><li>Licensing and Technology Exploitation</li><li>Venture Formation and Startup</li><li>Venture Financing</li><li>Creative Private Financing Arrangements</li><li>Mergers and Acquisitions</li><li>Real Estate</li><li>Contacts</li></ul>
  <ul class="abs foot-list" style="left:490px"><li>Audits</li><li>Analyses</li><li>Legal Project Management</li><li>Local Counsel for Transactions<br>and Due Diligence</li><li>Vendor Management</li><li>Dispute Resolution</li><li>Service as a Mediator or Arbitrator</li></ul>
  <div class="abs foot-brand"><span class="brand-square"></span>QUELLANE</div>
  <div class="abs copyright">© Copyright 2014</div>
</footer>

</body>
</html>
```